Product Line Brochure

Would like to have a bifold brochure for our product line to show to customers. Would like it to incorporate the paragraph description of the product line with the picture, followed by the product listings. I would like the brochure to be clean and modern. We are a specialty chemical manufacturer in NJ area.

```html
<!DOCTYPE html>
<html lang="en">
<head>
<meta charset="utf-8">
<title>Meridian Polymer Co. – Product Line Brochure</title>
<link href="https://fonts.googleapis.com/css2?family=Oswald:wght@400;500;600&family=Roboto:wght@400;500;700&display=swap" rel="stylesheet">
<style>
:root{
  --blue:#2e3192;
  --red:#d71920;
  --red-dark:#b3141a;
  --ink:#333;
  --muted:#777;
  --rule:#e3e3e3;
  --thumb:#c9c9c9;
  --stage:#e5e5e5;
  --paper:#ffffff;
  --head:'Oswald',sans-serif;
  --body:'Roboto',sans-serif;
}
*{box-sizing:border-box;margin:0;padding:0}
html,body{width:1200px;height:2378px;overflow:hidden;background:var(--stage)}
body{font-family:var(--body);color:var(--ink)}
.canvas{position:relative;width:1200px;height:2378px;overflow:hidden;background:var(--stage)}

.caption{position:absolute;font-family:var(--body);font-size:22px;color:#3a3a3a}

/* ---------- covers ---------- */
.cover{position:absolute;top:50px;width:400px;height:566px;background:var(--paper);overflow:hidden;box-shadow:0 10px 26px rgba(0,0,0,.18)}
.cover--back{left:150px}
.cover--front{left:650px}
.cover svg.bg{position:absolute;inset:0}

.brand{display:flex;align-items:center;gap:6px;font-family:var(--head);font-weight:600;color:var(--blue);text-transform:uppercase;letter-spacing:.5px}
.brand__mark{width:10px;height:10px;background:var(--red)}

.front__photo{position:absolute;left:110px;top:0;width:290px;height:330px;background:linear-gradient(160deg,#f4f6f8 0%,#dfe4ea 45%,#c8d0d9 100%)}
.front__brand{position:absolute;left:34px;top:40px;font-size:19px}
.front__band{position:absolute;left:0;right:0;bottom:0;height:200px;padding:62px 30px 0 28px;color:#fff}
.front__title{font-family:var(--head);font-weight:600;font-size:24px;letter-spacing:.5px}
.front__tag{font-size:7.5px;line-height:1.55;margin-top:8px;max-width:240px;text-transform:uppercase;font-weight:500}
.front__web{position:absolute;right:26px;top:318px;font-size:8px;color:var(--blue)}

.back__about{position:absolute;left:0;top:0;width:400px;height:260px;padding:40px 28px 0;color:#fff}
.back__h{font-family:var(--head);font-size:24px;font-weight:500;letter-spacing:.5px}
.back__lead{font-size:7.5px;line-height:1.6;margin-top:8px;max-width:330px}
.back__fields{display:grid;grid-template-columns:repeat(3,auto);gap:12px 16px;margin-top:16px;font-size:7.5px;list-style:none}
.back__fields li{display:flex;align-items:center;gap:6px}
.ico{width:16px;height:16px;border-radius:50%;background:var(--red);display:inline-flex;align-items:center;justify-content:center;flex:none}
.back__mid{position:absolute;left:0;top:268px;width:400px;height:160px;padding:0 28px;display:grid;grid-template-columns:1fr 1fr;gap:20px}
.back__mid h3{font-family:var(--head);font-size:13px;color:var(--red);font-weight:500;margin-bottom:6px}
.back__mid p{font-size:6.5px;line-height:1.6;color:var(--ink)}
.back__brand{position:absolute;right:28px;top:398px;font-size:12px}
.back__contact{position:absolute;left:0;bottom:0;width:400px;height:130px;padding:18px 28px;color:#fff}
.back__contact h3{font-family:var(--head);font-size:15px;font-weight:500;margin-bottom:8px}
.back__contact ul{list-style:none;font-size:7.5px;line-height:1}
.back__contact li{display:flex;align-items:center;gap:6px;margin-bottom:6px}
.cico{width:11px;height:11px;border-radius:50%;background:#fff;display:inline-flex;align-items:center;justify-content:center}

/* ---------- spreads ---------- */
.spread{position:absolute;width:540px;height:390px;display:flex;box-shadow:0 10px 24px rgba(0,0,0,.18)}
.page{position:relative;width:270px;height:390px;background:var(--paper);overflow:hidden}
.page + .page{border-left:1px solid #ececec}
.page svg.bg{position:absolute;inset:0}
.page__inner{position:relative;padding:52px 16px 0}
.section-title{position:absolute;left:14px;top:19px;font-family:var(--head);font-size:13px;font-weight:500;color:#fff;letter-spacing:.4px;text-transform:uppercase}
.sub{font-family:var(--head);font-size:9px;font-weight:500;color:var(--blue);text-transform:uppercase;letter-spacing:.3px}
.intro{font-size:5.5px;line-height:1.6;color:var(--muted);margin:4px 0 10px}
.tbl-title{font-size:7.5px;font-weight:700;color:var(--blue);margin:4px 0 4px}
.tbl-title em{font-style:normal;color:var(--red);font-weight:500}
table.products{width:100%;border-collapse:collapse;font-size:5.3px;color:var(--ink)}
.products th{text-align:left;font-weight:700;color:var(--blue);padding:2px 2px 4px;border-bottom:1px solid var(--rule)}
.products td{padding:4px 2px;border-bottom:1px solid var(--rule);vertical-align:middle;line-height:1.4}
.products td:last-child{color:var(--muted);width:38%}
.thumb{display:block;width:22px;height:22px;background:var(--thumb)}
.photo{position:absolute;left:14px;right:14px;bottom:30px;height:150px}
.foot{position:absolute;left:14px;right:14px;bottom:10px;font-size:4.5px;color:var(--muted);display:flex;justify-content:space-between}
.pg{position:absolute;bottom:8px;width:12px;height:9px;background:var(--red);color:#fff;font-size:5px;display:flex;align-items:center;justify-content:center}
.page--left .pg{left:0}
.page--right .pg{right:0}

.presence{text-align:center;padding-top:40px}
.presence .brand{justify-content:center;font-size:13px}
.presence__h{font-family:var(--head);font-size:14px;color:var(--blue);font-weight:500;margin-top:8px}
.presence__sub{font-family:var(--head);font-size:11px;color:var(--red);font-weight:500}
.presence__line{font-size:5.5px;color:var(--muted);margin-top:3px;text-transform:uppercase}
.map{position:absolute;left:16px;top:150px;width:160px;height:120px;background:linear-gradient(180deg,#f2f2f2,#dcdcdc)}
.legend{position:absolute;left:186px;top:160px;list-style:none;font-size:5px;color:var(--ink);text-align:left}
.legend li{display:flex;align-items:center;gap:4px;margin-bottom:5px}
.legend i{width:5px;height:5px;border-radius:50%;background:var(--red);display:inline-block}
.legend li.hq i{background:var(--blue)}
</style>
</head>
<body>
<main class="canvas">

  <!-- Back cover -->
  <section class="cover cover--back">
    <svg class="bg" width="400" height="566" viewBox="0 0 400 566" aria-hidden="true">
      <polygon points="0,0 400,0 400,232 0,262" fill="var(--blue)"/>
      <polygon points="0,262 400,232 400,240 0,270" fill="var(--red)"/>
      <polygon points="0,436 400,420 400,566 0,566" fill="var(--red)"/>
    </svg>
    <div class="back__about">
      <h2 class="back__h">ABOUT US</h2>
      <p class="back__lead">Meridian Polymer Co. has produced specialty chemicals for almost 40 years. We combine a wealth of expertise with R&amp;D capability and the responsiveness of our technical and customer service team to support our customers.</p>
      <ul class="back__fields">
        <li><span class="ico"><svg width="8" height="8"><rect x="1" y="2" width="6" height="5" fill="#fff"/></svg></span>Architectural</li>
        <li><span class="ico"><svg width="8" height="8"><rect x="1" y="1" width="6" height="6" fill="#fff"/></svg></span>Textiles &amp; Leather</li>
        <li><span class="ico"><svg width="8" height="8"><circle cx="4" cy="4" r="3" fill="#fff"/></svg></span>Inks, Paints &amp; Coatings</li>
        <li><span class="ico"><svg width="8" height="8"><polygon points="4,1 7,7 1,7" fill="#fff"/></svg></span>Adhesives/Adhesion Promoters</li>
        <li><span class="ico"><svg width="8" height="8"><rect x="2" y="1" width="4" height="6" fill="#fff"/></svg></span>Industries including</li>
      </ul>
    </div>
    <div class="back__mid">
      <div>
        <h3>40 YEARS OF EXPERIENCE</h3>
        <p>Founded in New Jersey, we have grown into a trusted supplier of specialty additives, repellents and adhesion promoters for manufacturers across many industries and markets.</p>
      </div>
      <div>
        <h3>DEDICATION TO OUR CUSTOMERS</h3>
        <p>Our chemists work closely with each customer to tailor products to their process, offering samples, technical data and hands-on support from first trial through full production runs.</p>
      </div>
    </div>
    <div class="brand back__brand"><span class="brand__mark"></span>Meridian Polymer Co.</div>
    <div class="back__contact">
      <h3>CONTACT US</h3>
      <ul>
        <li><span class="cico"><svg width="7" height="7" viewBox="0 0 10 10"><path d="M5 1a3 3 0 0 1 3 3c0 2-3 5-3 5S2 6 2 4a3 3 0 0 1 3-3z" fill="var(--red)"/></svg></span>218 Harbor Works Road, Linden, NJ 07036</li>
        <li><span class="cico"><svg width="7" height="7" viewBox="0 0 10 10"><path d="M2 1h2l1 2-1 1a5 5 0 0 0 2 2l1-1 2 1v2c-4 0-7-3-7-7z" fill="var(--red)"/></svg></span>+1 (908) 555 0142</li>
        <li><span class="cico"><svg width="7" height="7" viewBox="0 0 10 10"><path d="M2 1h2l1 2-1 1a5 5 0 0 0 2 2l1-1 2 1v2c-4 0-7-3-7-7z" fill="var(--red)"/></svg></span>+1 (908) 555 0187</li>
        <li><span class="cico"><svg width="7" height="7" viewBox="0 0 10 10"><circle cx="5" cy="5" r="3.5" fill="none" stroke="var(--red)" stroke-width="1.2"/><line x1="1.5" y1="5" x2="8.5" y2="5" stroke="var(--red)"/></svg></span>www.meridianpolymer.example</li>
      </ul>
    </div>
  </section>
  <div class="caption" style="left:375px;top:624px">Back</div>

  <!-- Front cover -->
  <section class="cover cover--front">
    <div class="front__photo" role="img" aria-label="Clear laboratory glassware and beakers on a white bench"></div>
    <svg class="bg" width="400" height="566" viewBox="0 0 400 566" aria-hidden="true">
      <polygon points="0,0 150,0 0,330" fill="var(--blue)"/>
      <polygon points="0,0 130,0 0,290" fill="#fff" opacity=".0"/>
      <polygon points="0,390 400,336 400,566 0,566" fill="var(--red)"/>
      <line x1="0" y1="380" x2="400" y2="326" stroke="var(--blue)" stroke-width="2"/>
    </svg>
    <div class="brand front__brand" style="background:#fff;padding:6px 10px"><span class="brand__mark"></span>Meridian Polymer Co.</div>
    <div class="front__web">www.meridianpolymer.example</div>
    <div class="front__band">
      <h1 class="front__title">MERIDIAN POLYMER CO.</h1>
      <p class="front__tag">Offering a range of specialty chemicals designed for use across a broad spectrum of products and industries</p>
    </div>
  </section>
  <div class="caption" style="left:820px;top:624px">Front</div>

  <!-- Spread 1 -->
  <section class="spread" style="left:40px;top:700px">
    <div class="page page--left">
      <svg class="bg" width="270" height="390" aria-hidden="true"><rect width="270" height="8" fill="var(--red)"/><polygon points="0,14 210,14 196,40 0,40" fill="var(--red)"/><line x1="14" y1="374" x2="270" y2="374" stroke="var(--red)"/></svg>
      <h2 class="section-title">Architectural Applications</h2>
      <div class="page__inner">
        <h3 class="sub">Water, Oil &amp; Stain Repellents</h3>
        <p class="intro">Protective treatments for concrete, stone, brick and wood that shed water, oil and stains while letting surfaces breathe.</p>
        <p class="tbl-title">Water, Oil &amp; Stain Repellents <em>– Waterborne</em></p>
        <table class="products"><tr><th></th><th>Product</th><th>Solvent</th><th>Solids %</th><th>Description</th></tr>
          <tr><td><span class="thumb"></span></td><td>MP-Guard 210</td><td>Water</td><td>30</td><td>Penetrating repellent for masonry.</td></tr>
          <tr><td><span class="thumb"></span></td><td>MP-Guard 225</td><td>Water</td><td>25</td><td>Oil and stain block for stone.</td></tr>
          <tr><td><span class="thumb"></span></td><td>MP-Guard 240</td><td>Water</td><td>20</td><td>Clear sealer for porous concrete.</td></tr>
          <tr><td><span class="thumb"></span></td><td>MP-Guard 260</td><td>Water</td><td>15</td><td>Low odor treatment for wood.</td></tr>
        </table>
      </div>
      <div class="foot"><span>Copyright © 2024 Meridian Polymer Co. All Rights Reserved.</span><span>www.meridianpolymer.example</span></div>
      <span class="pg">02</span>
    </div>
    <div class="page page--right">
      <svg class="bg" width="270" height="390" aria-hidden="true"><rect width="270" height="8" fill="var(--red)"/><polygon points="60,14 270,14 270,22 56,22" fill="var(--red)"/><line x1="0" y1="374" x2="256" y2="374" stroke="var(--red)"/></svg>
      <div class="page__inner" style="padding-top:32px">
        <p class="tbl-title">Water, Oil &amp; Stain Repellents <em>– Solventborne</em></p>
        <table class="products"><tr><th>Product</th><th>Solvent</th><th>Solids %</th><th>Description</th></tr>
          <tr><td>MP-Guard 310</td><td>Mineral spirits</td><td>10</td><td>Deep penetrating repellent for brick.</td></tr>
          <tr><td>MP-Guard 330</td><td>Acetate</td><td>8</td><td>Fast drying stain guard for tile.</td></tr>
        </table>
      </div>
      <div class="photo" role="img" aria-label="Water droplet beading on a brown textured surface" style="background:radial-gradient(circle at 55% 45%,#a38b78 0%,#6e5646 45%,#3f2f25 100%)"></div>
      <div class="foot"><span>Copyright © 2024 Meridian Polymer Co.</span><span>www.meridianpolymer.example</span></div>
      <span class="pg">03</span>
    </div>
  </section>
  <div class="caption" style="left:258px;top:1104px">Inner Side 1</div>

  <!-- Spread 2 -->
  <section class="spread" style="left:620px;top:700px">
    <div class="page page--left">
      <svg class="bg" width="270" height="390" aria-hidden="true"><rect width="270" height="8" fill="var(--red)"/><polygon points="0,14 180,14 166,40 0,40" fill="var(--red)"/><line x1="14" y1="374" x2="270" y2="374" stroke="var(--red)"/></svg>
      <h2 class="section-title">Textiles &amp; Leather</h2>
      <div class="page__inner">
        <h3 class="sub">Fabric &amp; Leather Protectants</h3>
        <p class="intro">Durable finishes that keep fabrics and leather clean and dry without changing their feel or colour.</p>
        <p class="tbl-title">Fabric &amp; Leather Protectants <em>– Waterborne</em></p>
        <table class="products"><tr><th></th><th>Product</th><th>Solvent</th><th>Solids %</th><th>Description</th></tr>
          <tr><td><span class="thumb"></span></td><td>MP-Tex 110</td><td>Water</td><td>30</td><td>Repellent finish for apparel.</td></tr>
          <tr><td><span class="thumb"></span></td><td>MP-Tex 120</td><td>Water</td><td>25</td><td>Soil release for upholstery.</td></tr>
          <tr><td><span class="thumb"></span></td><td>MP-Tex 135</td><td>Water</td><td>20</td><td>Protectant for leather goods.</td></tr>
          <tr><td><span class="thumb"></span></td><td>MP-Tex 150</td><td>Water</td><td>18</td><td>Durable rain wear finish.</td></tr>
          <tr><td><span class="thumb"></span></td><td>MP-Tex 170</td><td>Water</td><td>12</td><td>Spray protectant for carpets.</td></tr>
        </table>
      </div>
      <div class="foot"><span>Copyright © 2024 Meridian Polymer Co. All Rights Reserved.</span><span>www.meridianpolymer.example</span></div>
      <span class="pg">04</span>
    </div>
    <div class="page page--right">
      <svg class="bg" width="270" height="390" aria-hidden="true"><rect width="270" height="8" fill="var(--red)"/><polygon points="60,14 270,14 270,22 56,22" fill="var(--red)"/><line x1="0" y1="374" x2="256" y2="374" stroke="var(--red)"/></svg>
      <div class="page__inner" style="padding-top:32px">
        <p class="tbl-title">Fabric &amp; Leather Protectants <em>– Solventborne</em></p>
        <table class="products"><tr><th>Product</th><th>Solvent</th><th>Solids %</th><th>Description</th></tr>
          <tr><td>MP-Tex 210</td><td>Mineral spirits</td><td>10</td><td>Aerosol guard for suede and nubuck.</td></tr>
          <tr><td>MP-Tex 230</td><td>Acetate</td><td>6</td><td>Clear repellent for technical fabrics.</td></tr>
        </table>
      </div>
      <div class="photo" role="img" aria-label="Water drops beading on blue fabric" style="background:radial-gradient(circle at 50% 50%,#3b5fb0 0%,#1f3a85 55%,#0f1f55 100%)"></div>
      <div class="foot"><span>Copyright © 2024 Meridian Polymer Co.</span><span>www.meridianpolymer.example</span></div>
      <span class="pg">05</span>
    </div>
  </section>
  <div class="caption" style="left:838px;top:1104px">Inner Side 2</div>

  <!-- Spread 3 -->
  <section class="spread" style="left:40px;top:1260px">
    <div class="page page--left">
      <svg class="bg" width="270" height="390" aria-hidden="true"><rect width="270" height="8" fill="var(--red)"/><polygon points="0,14 190,14 176,40 0,40" fill="var(--red)"/><line x1="14" y1="374" x2="270" y2="374" stroke="var(--red)"/></svg>
      <h2 class="section-title">Inks, Paints &amp; Coatings</h2>
      <div class="page__inner">
        <h3 class="sub">Various Additives</h3>
        <p class="intro">Performance additives that improve repellency, flow and surface feel in inks, paints and industrial coatings.</p>
        <p class="tbl-title">Water Repellents</p>
        <table class="products"><tr><th></th><th>Product</th><th>Solvent</th><th>Solids %</th><th>Description</th></tr>
          <tr><td><span class="thumb"></span></td><td>MP-Coat 410</td><td>Water</td><td>40</td><td>Additive for latex wall paints.</td></tr>
          <tr><td><span class="thumb"></span></td><td>MP-Coat 420</td><td>Water</td><td>35</td><td>Beading agent for clear coats.</td></tr>
          <tr><td><span class="thumb"></span></td><td>MP-Coat 435</td><td>Glycol</td><td>30</td><td>Repellent for printing inks.</td></tr>
          <tr><td><span class="thumb"></span></td><td>MP-Coat 450</td><td>Water</td><td>25</td><td>Additive for wood stains.</td></tr>
        </table>
      </div>
      <div class="foot"><span>Copyright © 2024 Meridian Polymer Co. All Rights Reserved.</span><span>www.meridianpolymer.example</span></div>
      <span class="pg">06</span>
    </div>
    <div class="page page--right">
      <svg class="bg" width="270" height="390" aria-hidden="true"><rect width="270" height="8" fill="var(--red)"/><polygon points="60,14 270,14 270,22 56,22" fill="var(--red)"/><line x1="0" y1="374" x2="256" y2="374" stroke="var(--red)"/></svg>
      <div class="page__inner" style="padding-top:32px">
        <p class="tbl-title">Oil/Slip Repellents</p>
        <table class="products"><tr><th>Product</th><th>Solvent</th><th>Solids %</th><th>Description</th></tr>
          <tr><td>MP-Coat 510</td><td>Acetate</td><td>20</td><td>Oil repellent for protective coatings.</td></tr>
          <tr><td>MP-Coat 530</td><td>Water</td><td>15</td><td>Slip additive for overprint varnish.</td></tr>
        </table>
      </div>
      <div class="photo" role="img" aria-label="Colourful paint and pigment close-up" style="background:linear-gradient(120deg,#3a1f2e 0%,#8a2f3d 30%,#2f7a7a 55%,#c98a2c 80%,#2b2340 100%)"></div>
      <div class="foot"><span>Copyright © 2024 Meridian Polymer Co.</span><span>www.meridianpolymer.example</span></div>
      <span class="pg">07</span>
    </div>
  </section>
  <div class="caption" style="left:258px;top:1664px">Inner Side 3</div>

  <!-- Spread 4 -->
  <section class="spread" style="left:620px;top:1260px">
    <div class="page page--left">
      <svg class="bg" width="270" height="390" aria-hidden="true"><rect width="270" height="8" fill="var(--red)"/><polygon points="0,14 190,14 176,40 0,40" fill="var(--red)"/><line x1="14" y1="374" x2="270" y2="374" stroke="var(--red)"/></svg>
      <h2 class="section-title">Inks, Paints &amp; Coatings</h2>
      <div class="page__inner">
        <p class="tbl-title">Wetting/Leveling Agents <em>– Hydrocarbons</em></p>
        <table class="products"><tr><th></th><th>Product</th><th>Solvent</th><th>Solids %</th><th>Description</th></tr>
          <tr><td><span class="thumb"></span></td><td>MP-Flow 610</td><td>Water</td><td>50</td><td>Wetting agent for waterborne inks.</td></tr>
          <tr><td><span class="thumb"></span></td><td>MP-Flow 620</td><td>Water</td><td>40</td><td>Leveling aid for floor finishes.</td></tr>
          <tr><td><span class="thumb"></span></td><td>MP-Flow 635</td><td>Glycol</td><td>35</td><td>Substrate wetting for plastics.</td></tr>
          <tr><td><span class="thumb"></span></td><td>MP-Flow 650</td><td>Water</td><td>30</td><td>Anti-crater additive for paint.</td></tr>
          <tr><td><span class="thumb"></span></td><td>MP-Flow 670</td><td>Water</td><td>25</td><td>Flow agent for can coatings.</td></tr>
        </table>
      </div>
      <div class="foot"><span>Copyright © 2024 Meridian Polymer Co. All Rights Reserved.</span><span>www.meridianpolymer.example</span></div>
      <span class="pg">08</span>
    </div>
    <div class="page page--right">
      <svg class="bg" width="270" height="390" aria-hidden="true"><rect width="270" height="8" fill="var(--red)"/><polygon points="60,14 270,14 270,22 56,22" fill="var(--red)"/><line x1="0" y1="374" x2="256" y2="374" stroke="var(--red)"/></svg>
      <div class="page__inner" style="padding-top:32px">
        <p class="tbl-title">Slip &amp; Abrasion</p>
        <table class="products"><tr><th>Product</th><th>Solvent</th><th>Solids %</th><th>Description</th></tr>
          <tr><td>MP-Slip 710</td><td>Water</td><td>35</td><td>Mar resistance for topcoats.</td></tr>
          <tr><td>MP-Slip 720</td><td>Acetate</td><td>30</td><td>Slip aid for printing inks.</td></tr>
          <tr><td>MP-Slip 740</td><td>Water</td><td>25</td><td>Abrasion resistance for lacquers.</td></tr>
        </table>
        <p class="tbl-title" style="margin-top:40px">Silane Coupling Agents <em>– Inorganic</em></p>
        <table class="products"><tr><th>Product</th><th>Solvent</th><th>Solids %</th><th>Description</th></tr>
          <tr><td>MP-Link 810</td><td>None</td><td>100</td><td>Coupling agent for glass fillers.</td></tr>
          <tr><td>MP-Link 830</td><td>Alcohol</td><td>50</td><td>Primer for metal and mineral bonds.</td></tr>
        </table>
      </div>
      <div class="foot"><span>Copyright © 2024 Meridian Polymer Co.</span><span>www.meridianpolymer.example</span></div>
      <span class="pg">09</span>
    </div>
  </section>
  <div class="caption" style="left:838px;top:1664px">Inner Side 4</div>

  <!-- Spread 5 -->
  <section class="spread" style="left:40px;top:1820px">
    <div class="page page--left">
      <svg class="bg" width="270" height="390" aria-hidden="true"><rect width="270" height="8" fill="var(--red)"/><polygon points="0,14 220,14 206,40 0,40" fill="var(--red)"/><line x1="14" y1="374" x2="270" y2="374" stroke="var(--red)"/></svg>
      <h2 class="section-title">Adhesives/Adhesion Promoters</h2>
      <div class="page__inner">
        <h3 class="sub">For Low Surface Energy Substrates</h3>
        <p class="intro">Promoters that help coatings, inks and adhesives bond to polyolefins and other hard to wet plastics.</p>
        <p class="tbl-title">Adhesion Promoters <em>– Waterborne</em></p>
        <table class="products"><tr><th></th><th>Product</th><th>Solvent</th><th>Solids %</th><th>Description</th></tr>
          <tr><td><span class="thumb"></span></td><td>MP-Bond 910</td><td>Water</td><td>30</td><td>Primer for polypropylene parts.</td></tr>
          <tr><td><span class="thumb"></span></td><td>MP-Bond 920</td><td>Water</td><td>25</td><td>Promoter for film laminates.</td></tr>
          <tr><td><span class="thumb"></span></td><td>MP-Bond 935</td><td>Water</td><td>20</td><td>Tie coat for flexible packaging.</td></tr>
          <tr><td><span class="thumb"></span></td><td>MP-Bond 950</td><td>Water</td><td>15</td><td>Adhesion aid for labels.</td></tr>
        </table>
      </div>
      <div class="foot"><span>Copyright © 2024 Meridian Polymer Co. All Rights Reserved.</span><span>www.meridianpolymer.example</span></div>
      <span class="pg">10</span>
    </div>
    <div class="page page--right">
      <svg class="bg" width="270" height="390" aria-hidden="true"><rect width="270" height="8" fill="var(--red)"/><polygon points="60,14 270,14 270,22 56,22" fill="var(--red)"/><line x1="0" y1="374" x2="256" y2="374" stroke="var(--red)"/></svg>
      <div class="page__inner" style="padding-top:32px">
        <p class="tbl-title">Adhesion Promoters <em>– Solventborne</em></p>
        <table class="products"><tr><th>Product</th><th>Solvent</th><th>Solids %</th><th>Description</th></tr>
          <tr><td>MP-Bond 1010</td><td>Xylene</td><td>20</td><td>Primer for automotive plastics.</td></tr>
          <tr><td>MP-Bond 1030</td><td>Acetate</td><td>15</td><td>Promoter for solvent inks on film.</td></tr>
        </table>
      </div>
      <div class="photo" role="img" aria-label="Amber adhesive strands stretching between surfaces" style="background:linear-gradient(180deg,#d9d2c4 0%,#b89a5e 50%,#8a6424 100%)"></div>
      <div class="foot"><span>Copyright © 2024 Meridian Polymer Co.</span><span>www.meridianpolymer.example</span></div>
      <span class="pg">11</span>
    </div>
  </section>
  <div class="caption" style="left:258px;top:2224px">Inner Side 5</div>

  <!-- Spread 6 -->
  <section class="spread" style="left:620px;top:1820px">
    <div class="page page--left">
      <svg class="bg" width="270" height="390" aria-hidden="true"><rect width="270" height="8" fill="var(--red)"/><polygon points="0,14 220,14 206,40 0,40" fill="var(--red)"/><line x1="14" y1="374" x2="270" y2="374" stroke="var(--red)"/></svg>
      <h2 class="section-title">Adhesives/Adhesion Promoters</h2>
      <div class="page__inner">
        <p class="tbl-title">Adhesion Promoters <em>– Solventborne</em></p>
        <table class="products"><tr><th></th><th>Product</th><th>Solvent</th><th>Solids %</th><th>Description</th></tr>
          <tr><td><span class="thumb"></span></td><td>MP-Bond 1110</td><td>Xylene</td><td>25</td><td>Primer for TPO bumpers.</td></tr>
          <tr><td><span class="thumb"></span></td><td>MP-Bond 1120</td><td>Toluene</td><td>20</td><td>Promoter for rubber bonding.</td></tr>
          <tr><td><span class="thumb"></span></td><td>MP-Bond 1135</td><td>Acetate</td><td>18</td><td>Clear primer for HDPE.</td></tr>
          <tr><td><span class="thumb"></span></td><td>MP-Bond 1150</td><td>Xylene</td><td>15</td><td>Tie coat for molded parts.</td></tr>
          <tr><td><span class="thumb"></span></td><td>MP-Bond 1170</td><td>Acetate</td><td>10</td><td>Primer for sealant joints.</td></tr>
        </table>
      </div>
      <div class="foot"><span>Copyright © 2024 Meridian Polymer Co. All Rights Reserved.</span><span>www.meridianpolymer.example</span></div>
      <span class="pg">12</span>
    </div>
    <div class="page page--right">
      <svg class="bg" width="270" height="390" aria-hidden="true"><rect width="270" height="8" fill="var(--red)"/><line x1="0" y1="374" x2="256" y2="374" stroke="var(--red)"/></svg>
      <div class="presence">
        <div class="brand"><span class="brand__mark"></span>Meridian Polymer Co.</div>
        <h2 class="presence__h">OUR PRESENCE</h2>
        <p class="presence__sub">TO PROVIDE EFFECTIVE SOLUTIONS</p>
        <p class="presence__line">Through technical innovation &amp; exemplary service</p>
      </div>
      <div class="map" role="img" aria-label="Map of the United States marking company locations"></div>
      <ul class="legend">
        <li class="hq"><i></i>Headquarters</li>
        <li><i></i>Distribution</li>
        <li><i></i>Sales Office</li>
      </ul>
      <span class="pg">13</span>
    </div>
  </section>
  <div class="caption" style="left:838px;top:2224px">Inner Side 6</div>

</main>
</body>
</html>
```